Business cards for Paperleaf Sprites

Please note that the color of the logo has been changed from green to teal blue. Sorry for the changing!

Anything will go but want to have some funky side.

I would like the front of the business card is the logo and business information and the back side is the Adult Coloring, so that would attract the customer to do the coloring on the other side. Have more interactive side. (pictures for references only can see it below). Fairies on the back of the card for coloring and whatever you want to adds on to color, like flowers, nature etc......

Scrapbooking is not just paper, it also involves watercolor, mixed media, art, all the fun stuff.

Another keypoint I would like to stress on is the back of the business card should be Adult Coloring and make sure you are not google and use the search engine to copy and paste because of the copyright issue.

As a designer, I am sure you all can create beautiful artwork.

Please submit your creativities!

Want the business card is out of the ordinary and customers would like to keep that as a keepsake rather than treat like a regular business card and trash it. Fonts cannot be too small, consider some of the customers have to wear bi-focal eyeglasses.

Thanks a lot!

Target Market(s)

Scrapbooking, Card making, papercraft, stampin‘ , gifts items , etc.

Industry/Entity Type

Retail

Contact Information for Business Card

Color Scheme, please match with the Logo. Watercolor effect is nice!
Thanks!

Font styles to use
Serif

Requirements
Must have
• I would like Elegant and playful.
• Thanks!
Nice to have
• Watercolor effect or check out the Adult Coloring Book, I am thinking we can use a double-sided business card, one side for the information and the other side for people can do the coloring. I have attached 2 pictures for reference.
Should not have
• No black color on the background please!

```html
<!DOCTYPE html>
<html lang="en">
<head>
<meta charset="utf-8">
<title>Paperleaf Sprites – Business Card</title>
<link rel="stylesheet" href="https://fonts.googleapis.com/css2?family=Arimo:wght@400;700&family=Tinos&display=swap">
<style>
  :root {
    --page-bg: #ece8e4;
    --card-bg: #ffffff;
    --teal: #3a8d9c;
    --teal-dark: #2f7886;
    --crimson: #b3262f;
    --ink-gray: #5b5b5b;
    --text-gray: #444444;
  }
  * { margin: 0; padding: 0; box-sizing: border-box; }
  html, body {
    width: 1200px;
    height: 1000px;
    overflow: hidden;
    background: var(--page-bg);
  }
  .canvas {
    position: relative;
    width: 1200px;
    height: 1000px;
  }
  .business-card {
    position: absolute;
    left: 100px;
    top: 222px;
    width: 1000px;
    height: 556px;
    background: var(--card-bg);
    box-shadow: 0 6px 24px rgba(0,0,0,0.12);
    overflow: hidden;
  }
  .brand-band {
    position: absolute;
    left: 0;
    top: 135px;
    width: 100%;
    height: 86px;
  }
  .brand-band svg { display: block; }
  .brand-name {
    position: absolute;
    left: 0;
    top: 135px;
    width: 100%;
    height: 86px;
    display: flex;
    align-items: center;
    justify-content: center;
    font-family: "Arimo", Arial, sans-serif;
    font-weight: 700;
    font-size: 44px;
    letter-spacing: 2px;
    color: #ffffff;
  }
  .side-tab {
    position: absolute;
    left: 0;
    top: 324px;
    width: 20px;
    height: 90px;
    background: var(--teal);
    border-radius: 0 10px 10px 0;
  }
  .person-name {
    position: absolute;
    left: 42px;
    top: 326px;
    font-family: "Arimo", Arial, sans-serif;
    font-size: 41px;
    line-height: 48px;
  }
  .person-name .first { color: var(--teal); }
  .person-name .last { color: var(--ink-gray); }
  .person-role {
    position: absolute;
    left: 42px;
    top: 372px;
    font-family: "Arimo", Arial, sans-serif;
    font-size: 24px;
    letter-spacing: 5px;
    color: var(--text-gray);
  }
  .contact-line {
    position: absolute;
    left: 665px;
    display: flex;
    align-items: center;
    gap: 24px;
    color: var(--text-gray);
  }
  .contact-line svg { width: 28px; height: 28px; flex: none; }
  .contact-phone { top: 409px; font-family: "Tinos", "Times New Roman", serif; font-size: 23px; }
  .contact-email { top: 456px; font-family: "Arimo", Arial, sans-serif; font-size: 21px; }
</style>
</head>
<body>
<div class="canvas">
  <div class="business-card">
    <div class="brand-band">
      <svg width="1000" height="86" viewBox="0 0 1000 86">
        <rect x="0" y="0" width="1000" height="2" fill="var(--crimson)"/>
        <rect x="0" y="5" width="1000" height="1" fill="var(--crimson)"/>
        <rect x="0" y="9" width="1000" height="68" fill="var(--teal)"/>
        <rect x="0" y="80" width="1000" height="1" fill="var(--crimson)"/>
        <rect x="0" y="84" width="1000" height="2" fill="var(--crimson)"/>
      </svg>
    </div>
    <div class="brand-name">Paperleaf Sprites</div>

    <div class="side-tab"></div>
    <div class="person-name"><span class="first">Mira</span><span class="last">Calloway</span></div>
    <div class="person-role">Designer</div>

    <div class="contact-line contact-phone">
      <svg viewBox="0 0 28 28" aria-hidden="true">
        <rect width="28" height="28" rx="4" fill="var(--teal)"/>
        <path d="M9 6.5c1 0 1.6.3 2 1.2l1.2 2.6c.3.7.1 1.3-.4 1.8l-1 .9c.8 1.8 2 3 3.8 3.9l.9-1c.5-.5 1.1-.7 1.8-.4l2.6 1.2c.9.4 1.2 1 1.2 2 0 2-1.7 3.3-3.6 3.1C11.6 21.1 6.9 16.4 6.3 10.5 6.1 8.6 7.3 6.5 9 6.5z" fill="#fff"/>
      </svg>
      <span>0123-456-789</span>
    </div>
    <div class="contact-line contact-email">
      <svg viewBox="0 0 28 28" aria-hidden="true">
        <rect width="28" height="28" rx="4" fill="var(--teal)"/>
        <rect x="6" y="8.5" width="16" height="11" fill="none" stroke="#fff" stroke-width="1.6"/>
        <path d="M6 8.5l8 6.5 8-6.5M6 19.5l6-5M22 19.5l-6-5" fill="none" stroke="#fff" stroke-width="1.4"/>
      </svg>
      <span>Name@website.com</span>
    </div>
  </div>
</div>
</body>
</html>
```